"Nine Pals Per Month" - a blog by 7+ writers about multiple topics with constantly fresh content

Need a good design for a new WordPress blog... Nine Pals per Month will be a blog written by seven bloggers. The idea is to have a a bunch of different writers providing content more frequently than a single writer can. It also means that content will be different from writer to writer. The blog is intended to be fun and not too serious.
Target Market(s)
The audience for this blog is wide open. Having different writers with different interests and styles means that the topics will be different all the time. This blog will not be too serious or self-important. It is intended to be light hearted and fun.
Look and feel
Each slider illustrates characteristics of the customer's brand and the style your logo design should communicate.

```html
<!DOCTYPE html>
<html lang="en">
<head>
<meta charset="utf-8">
<title>Nine Pals Per Month</title>
<link rel="stylesheet" href="https://fonts.googleapis.com/css2?family=Open+Sans:wght@400;600;700&display=swap">
<style>
:root{
  --red:#c3202e;
  --ink:#222;
  --muted:#8a8a8a;
  --line:#e2e2e2;
  --card:#f1f1f1;
  --band:#f4f4f4;
  --foot:#2b2b2b;
  --foot-dark:#1f1f1f;
  --menu:rgba(60,52,62,.72);
}
*{margin:0;padding:0;box-sizing:border-box}
html,body{width:1200px;height:2691px;overflow:hidden}
body{font-family:"Open Sans",Arial,sans-serif;color:var(--ink);background:#fff;position:relative}
.abs{position:absolute}
/* hero */
.hero{left:0;top:0;width:1200px;height:614px;background:linear-gradient(180deg,#e07a56 0%,#e9a27c 30%,#b98c95 48%,#6f6a8c 70%,#3d4b73 100%)}
.site-header{left:131px;top:0;width:936px;height:97px;background:#fff}
.brand{left:20px;top:28px;display:flex;align-items:center;gap:10px;font-weight:700;font-size:21px;color:var(--red);line-height:1}
.brand i{display:block;width:16px;height:16px;background:var(--red)}
.socials{right:14px;top:18px;display:flex;gap:5px}
.socials span{width:25px;height:25px;border-radius:50%;display:block}
.main-nav{right:16px;top:58px;display:flex;gap:34px;font-size:12px;color:#666}
.main-nav .active{color:var(--red)}
.hero-title{left:624px;top:168px;font-size:26px;font-weight:600;color:#151515}
.cat-menu{left:133px;top:131px;width:170px}
.cat-item{height:60px;margin-bottom:5px;display:flex;align-items:center;background:var(--menu);color:#fff;font-size:13px}
.cat-item .ico{width:60px;height:60px;display:flex;align-items:center;justify-content:center;background:rgba(30,28,36,.55)}
.cat-item .label{padding-left:14px}
.cat-item.active{background:#fff;color:var(--red)}
.cat-item.active .ico{background:var(--red)}
/* section head */
.section-title{left:0;width:1200px;top:644px;text-align:center;font-size:34px;color:var(--red);display:flex;justify-content:center;align-items:center;gap:12px}
.rule{left:131px;top:716px;width:936px;height:1px;background:var(--line)}
.col-head{font-size:22px;color:var(--ink);padding-bottom:6px}
.featured-head{left:131px;top:748px;width:222px;color:var(--red);border-bottom:3px solid var(--red)}
.recent-head{left:388px;top:748px;width:679px;border-bottom:3px solid #222}
/* featured */
.feat{left:131px;width:222px}
.photo{display:block}
.feat .photo{height:135px}
.feat h3{font-size:13px;font-weight:400;color:var(--red);line-height:19px;margin-top:14px}
.feat p{font-size:9.5px;color:var(--muted);line-height:14.5px;margin-top:8px;text-align:justify}
.date{display:inline-block;background:#e8e8e8;color:#888;font-size:9px;padding:5px 12px}
.feat .date{margin-top:12px}
.promo{left:131px;top:1749px;width:222px;height:175px;background:linear-gradient(180deg,#4a4a4c,#8c8c8e)}
.promo span{position:absolute;left:0;bottom:0;width:100%;height:40px;background:rgba(220,220,220,.85);text-align:center;line-height:40px;font-weight:700;font-size:16px;color:#222}
/* recent */
.post{left:388px;width:679px;height:247px;background:var(--card)}
.post .photo{position:absolute;left:0;top:0;width:262px;height:247px}
.post .body{position:absolute;left:286px;top:24px;width:370px}
.post h3{font-size:13px;font-weight:400;color:var(--red);line-height:20px}
.post p{font-size:9.5px;color:var(--muted);line-height:14.5px;margin-top:10px;text-align:justify}
.post .meta{position:absolute;left:286px;top:193px;display:flex;align-items:center;gap:14px}
.pager{left:388px;top:1893px;display:flex;gap:6px}
.pager span{width:32px;height:32px;border-radius:50%;background:#e6e6e6;color:#888;font-size:10px;display:flex;align-items:center;justify-content:center}
.pager .on{background:var(--red);color:#fff}
/* other posts */
.band{left:0;top:1977px;width:1200px;height:481px;background:var(--band)}
.band-title{left:0;top:2005px;width:1200px;text-align:center;font-size:30px;color:var(--red)}
.other{top:2077px;width:290px}
.other .photo{height:182px}
.other h3{font-size:13px;font-weight:400;line-height:19px;margin-top:16px;color:#222}
.other p{font-size:9.5px;color:var(--muted);line-height:15px;margin-top:10px;text-align:justify}
.other .more{font-size:9.5px;font-weight:600;margin-top:16px;color:#222}
/* footer */
.footer{left:0;top:2458px;width:1200px;height:176px;background:var(--foot);color:#ddd}
.footer h4{font-size:12px;font-weight:600;color:#eee}
.footer ul{list-style:none;font-size:10.5px;color:#999;line-height:22.5px;margin-top:10px}
.footer li:before{content:"•";margin-right:6px;color:#777}
.vline{top:30px;width:1px;height:120px;background:#3c3c3c}
.news{left:635px;top:62px;width:218px;height:36px;background:#fff;font-size:10px;color:#777;padding:12px 14px}
.news b{position:absolute;right:0;top:0;width:26px;height:36px;background:var(--red)}
.f-soc{left:930px;top:64px;display:flex;gap:6px}
.f-soc span{width:26px;height:26px;border-radius:50%;display:block}
.copy{left:0;top:2634px;width:1200px;height:57px;background:var(--foot-dark);color:#999;font-size:10.5px;text-align:center;line-height:57px}
</style>
</head>
<body>

<div class="abs hero" role="img" aria-label="Sunset over calm sea with a wooden pier and a photographer standing in shallow water"></div>

<header class="abs site-header">
  <div class="abs brand"><i></i>Nine Pals Per Month</div>
  <div class="abs socials">
    <span style="background:#3b5998"></span><span style="background:#1da1f2"></span><span style="background:#0e76a8"></span><span style="background:#dd4b39"></span><span style="background:#cb2027"></span><span style="background:#f57d00"></span><span style="background:#d62d2d"></span><span style="background:#3f729b"></span><span style="background:#5fa33c"></span>
  </div>
  <nav class="abs main-nav"><span class="active">Home</span><span>Blog Categories</span><span>About us</span><span>Contact us</span></nav>
</header>

<h1 class="abs hero-title">Cras dignissim bibendum accumsan</h1>

<nav class="abs cat-menu">
  <div class="cat-item active"><span class="ico"><svg width="22" height="18" viewBox="0 0 22 18"><rect x="1" y="4" width="20" height="13" rx="2" fill="#fff"/><rect x="7" y="1" width="8" height="4" fill="#fff"/><circle cx="11" cy="10.5" r="4" fill="#c3202e"/></svg></span><span class="label">Photography</span></div>
  <div class="cat-item"><span class="ico"><svg width="18" height="20" viewBox="0 0 18 20"><path d="M3 1v7h4V1M5 8v11M13 1c-3 2-3 8 0 9v9" stroke="#fff" stroke-width="2" fill="none"/></svg></span><span class="label">Food</span></div>
  <div class="cat-item"><span class="ico"><svg width="14" height="22" viewBox="0 0 14 22"><circle cx="7" cy="3" r="3" fill="#fff"/><path d="M3 7h8l2 8H1z M4 15h2v7H4z M8 15h2v7H8z" fill="#fff"/></svg></span><span class="label">Beauty</span></div>
  <div class="cat-item"><span class="ico"><svg width="20" height="18" viewBox="0 0 20 18"><path d="M10 17 2 9a4.6 4.6 0 0 1 8-5 4.6 4.6 0 0 1 8 5z" fill="#fff"/></svg></span><span class="label">RelationShips</span></div>
  <div class="cat-item"><span class="ico"><svg width="22" height="16" viewBox="0 0 22 16"><path d="M1 8h5l3-6 4 12 3-6h5" stroke="#fff" stroke-width="2" fill="none"/></svg></span><span class="label">Fitness</span></div>
  <div class="cat-item"><span class="ico"><svg width="22" height="18" viewBox="0 0 22 18"><circle cx="7" cy="10" r="5" stroke="#fff" stroke-width="3" fill="none" stroke-dasharray="3 2"/><circle cx="16" cy="5" r="3.5" stroke="#fff" stroke-width="2.5" fill="none" stroke-dasharray="2 1.5"/></svg></span><span class="label">Technology</span></div>
  <div class="cat-item"><span class="ico"><svg width="20" height="18" viewBox="0 0 20 18"><path d="M10 1 1 9h3v8h4v-5h4v5h4V9h3z" fill="#fff"/></svg></span><span class="label">Real Estate</span></div>
</nav>

<h2 class="abs section-title"><svg width="26" height="22" viewBox="0 0 22 18"><rect x="1" y="4" width="20" height="13" rx="2" fill="#c3202e"/><rect x="7" y="1" width="8" height="4" fill="#c3202e"/><circle cx="11" cy="10.5" r="4" fill="#fff"/></svg>Photography</h2>
<div class="abs rule"></div>

<h3 class="abs col-head featured-head">Featured Posts</h3>
<h3 class="abs col-head recent-head">Recent Posts</h3>

<article class="abs feat" style="top:795px">
  <div class="photo" role="img" aria-label="Close-up of a camera lens barrel" style="background:linear-gradient(135deg,#2a2a2a,#7a7a7a)"></div>
  <h3>Aliquam fermentum rutrum diam, ac gravida libero imperdiet sit amet.</h3>
  <p>Praesent vitae risus a magna imperdiet sollicitudin. Integer ut volutpat sapien, ut vestibulum velit. Fusce sit amet nibh rhoncus ipsum bibendum facilisis in eu lorem.</p>
  <span class="date">5 February, 2016</span>
</article>
<article class="abs feat" style="top:1112px">
  <div class="photo" role="img" aria-label="Studio lights on a brick wall set" style="background:linear-gradient(135deg,#3a2a22,#8a5a3c)"></div>
  <h3>Aliquam fermentum rutrum diam, ac gravida libero imperdiet sit amet.</h3>
  <p>Praesent vitae risus a magna imperdiet sollicitudin. Integer ut volutpat sapien, ut vestibulum velit. Fusce sit amet nibh rhoncus ipsum bibendum facilisis in eu lorem.</p>
  <span class="date">5 February, 2016</span>
</article>
<article class="abs feat" style="top:1428px">
  <div class="photo" role="img" aria-label="Curling ocean wave lit by the sun" style="background:linear-gradient(135deg,#2d4a4a,#c9a056)"></div>
  <h3>Aliquam fermentum rutrum diam, ac gravida libero imperdiet sit amet.</h3>
  <p>Praesent vitae risus a magna imperdiet sollicitudin. Integer ut volutpat sapien, ut vestibulum velit. Fusce sit amet nibh rhoncus ipsum bibendum facilisis in eu lorem.</p>
  <span class="date">5 February, 2016</span>
</article>
<div class="abs promo" role="img" aria-label="Camera lenses laid out on a grey surface"><span>NOVA LENSES</span></div>

<article class="abs post" style="top:795px">
  <div class="photo" role="img" aria-label="Vintage camera and pocket watch at sunset" style="background:linear-gradient(135deg,#6fa6c0,#d9b27a)"></div>
  <div class="body"><h3>Cras dignissim bibendum accumsan. Maecenas tristique felis id arcu adipiscing, ut viverra enim facilisis.</h3>
  <p>Aenean nec scelerisque est. Class aptent taciti sociosqu ad litora torquent per conubia nostra, per inceptos himenaeos. Ut ultricies felis et orci cursus feugiat. Interdum et malesuada fames ac ante ipsum primis in faucibus. Praesent lacinia sem leo, in vulputate neque vestibulum a. Sed lectus neque, egestas vitae ipsum vel, facilisis rhoncus nisi. Pellentesque non nisi molestie, vestibulum tellus at, congue velit. Integer consequat tortor a fermentum. Sed ultrices nisl at eros hendrerit, eu laoreet nisl bibendum.</p></div>
  <div class="meta"><span class="date">5 February, 2016</span><svg width="12" height="12" viewBox="0 0 12 12"><circle cx="9.5" cy="2.5" r="2" fill="#555"/><circle cx="2.5" cy="6" r="2" fill="#555"/><circle cx="9.5" cy="9.5" r="2" fill="#555"/><path d="M9.5 2.5 2.5 6l7 3.5" stroke="#555" fill="none"/></svg><svg width="13" height="11" viewBox="0 0 13 11"><ellipse cx="6.5" cy="4.5" rx="6" ry="4.2" fill="#555"/><path d="M3 7 2 11l4-3z" fill="#555"/></svg></div>
</article>
<article class="abs post" style="top:1068px">
  <div class="photo" role="img" aria-label="Photographer with tripod on a rocky ridge under a cloudy sky" style="background:linear-gradient(180deg,#a7b6c4,#4a4a4e)"></div>
  <div class="body"><h3>Cras dignissim bibendum accumsan. Maecenas tristique felis id arcu adipiscing, ut viverra enim facilisis.</h3>
  <p>Aenean nec scelerisque est. Class aptent taciti sociosqu ad litora torquent per conubia nostra, per inceptos himenaeos. Ut ultricies felis et orci cursus feugiat. Interdum et malesuada fames ac ante ipsum primis in faucibus. Praesent lacinia sem leo, in vulputate neque vestibulum a. Sed lectus neque, egestas vitae ipsum vel, facilisis rhoncus nisi. Pellentesque non nisi molestie, vestibulum tellus at, congue velit. Integer consequat tortor a fermentum. Sed ultrices nisl at eros hendrerit, eu laoreet nisl bibendum.</p></div>
  <div class="meta"><span class="date">5 February, 2016</span><svg width="12" height="12" viewBox="0 0 12 12"><circle cx="9.5" cy="2.5" r="2" fill="#555"/><circle cx="2.5" cy="6" r="2" fill="#555"/><circle cx="9.5" cy="9.5" r="2" fill="#555"/><path d="M9.5 2.5 2.5 6l7 3.5" stroke="#555" fill="none"/></svg><svg width="13" height="11" viewBox="0 0 13 11"><ellipse cx="6.5" cy="4.5" rx="6" ry="4.2" fill="#555"/><path d="M3 7 2 11l4-3z" fill="#555"/></svg></div>
</article>
<article class="abs post" style="top:1341px">
  <div class="photo" role="img" aria-label="Woman laughing under a colourful umbrella" style="background:linear-gradient(135deg,#5a7a3a,#c04a3a)"></div>
  <div class="body"><h3>Cras dignissim bibendum accumsan. Maecenas tristique felis id arcu adipiscing, ut viverra enim facilisis.</h3>
  <p>Aenean nec scelerisque est. Class aptent taciti sociosqu ad litora torquent per conubia nostra, per inceptos himenaeos. Ut ultricies felis et orci cursus feugiat. Interdum et malesuada fames ac ante ipsum primis in faucibus. Praesent lacinia sem leo, in vulputate neque vestibulum a. Sed lectus neque, egestas vitae ipsum vel, facilisis rhoncus nisi. Pellentesque non nisi molestie, vestibulum tellus at, congue velit. Integer consequat tortor a fermentum. Sed ultrices nisl at eros hendrerit, eu laoreet nisl bibendum.</p></div>
  <div class="meta"><span class="date">5 February, 2016</span><svg width="12" height="12" viewBox="0 0 12 12"><circle cx="9.5" cy="2.5" r="2" fill="#555"/><circle cx="2.5" cy="6" r="2" fill="#555"/><circle cx="9.5" cy="9.5" r="2" fill="#555"/><path d="M9.5 2.5 2.5 6l7 3.5" stroke="#555" fill="none"/></svg><svg width="13" height="11" viewBox="0 0 13 11"><ellipse cx="6.5" cy="4.5" rx="6" ry="4.2" fill="#555"/><path d="M3 7 2 11l4-3z" fill="#555"/></svg></div>
</article>
<article class="abs post" style="top:1614px">
  <div class="photo" role="img" aria-label="Hiker with red backpack taking a photo in the mountains" style="background:linear-gradient(135deg,#8fb0cc,#b94a3a)"></div>
  <div class="body"><h3>Cras dignissim bibendum accumsan. Maecenas tristique felis id arcu adipiscing, ut viverra enim facilisis.</h3>
  <p>Aenean nec scelerisque est. Class aptent taciti sociosqu ad litora torquent per conubia nostra, per inceptos himenaeos. Ut ultricies felis et orci cursus feugiat. Interdum et malesuada fames ac ante ipsum primis in faucibus. Praesent lacinia sem leo, in vulputate neque vestibulum a. Sed lectus neque, egestas vitae ipsum vel, facilisis rhoncus nisi. Pellentesque non nisi molestie, vestibulum tellus at, congue velit. Integer consequat tortor a fermentum. Sed ultrices nisl at eros hendrerit, eu laoreet nisl bibendum.</p></div>
  <div class="meta"><span class="date">5 February, 2016</span><svg width="12" height="12" viewBox="0 0 12 12"><circle cx="9.5" cy="2.5" r="2" fill="#555"/><circle cx="2.5" cy="6" r="2" fill="#555"/><circle cx="9.5" cy="9.5" r="2" fill="#555"/><path d="M9.5 2.5 2.5 6l7 3.5" stroke="#555" fill="none"/></svg><svg width="13" height="11" viewBox="0 0 13 11"><ellipse cx="6.5" cy="4.5" rx="6" ry="4.2" fill="#555"/><path d="M3 7 2 11l4-3z" fill="#555"/></svg></div>
</article>

<div class="abs pager"><span class="on">1</span><span>2</span><span>3</span><span>4</span><span>5</span><span>«</span><span>»</span></div>

<section class="abs band"></section>
<h2 class="abs band-title">Other Posts</h2>
<article class="abs other" style="left:131px">
  <div class="photo" role="img" aria-label="Runner leaping against a dramatic sky" style="background:linear-gradient(180deg,#c9ccd0,#3a3a3c)"></div>
  <h3>Aenean sed quam non sapien faucibus conse quat vitae sit amet orci.</h3>
  <p>Pellentesque blandit lacus eget nunc faucibus, et tincidunt eros viverra. Phasellus consequat sagittis nisi suscipit feugiat. Cras eget leo sed nunc hendrerit ultricies eu at nisl. Praesent iaculis faucibus urna sit amet lacinia.</p>
  <div class="more">READ MORE ▸</div>
</article>
<article class="abs other" style="left:456px">
  <div class="photo" role="img" aria-label="Hands holding a coconut bowl by the sea" style="background:linear-gradient(135deg,#3fb3b8,#e2b58e)"></div>
  <h3>Aenean sed quam non sapien faucibus conse quat vitae sit amet orci.</h3>
  <p>Pellentesque blandit lacus eget nunc faucibus, et tincidunt eros viverra. Phasellus consequat sagittis nisi suscipit feugiat. Cras eget leo sed nunc hendrerit ultricies eu at nisl. Praesent iaculis faucibus urna sit amet lacinia.</p>
  <div class="more">READ MORE ▸</div>
</article>
<article class="abs other" style="left:777px">
  <div class="photo" role="img" aria-label="Family smiling together outdoors" style="background:linear-gradient(135deg,#8a9a6a,#6a4a3a)"></div>
  <h3>Aenean sed quam non sapien faucibus conse quat vitae sit amet orci.</h3>
  <p>Pellentesque blandit lacus eget nunc faucibus, et tincidunt eros viverra. Phasellus consequat sagittis nisi suscipit feugiat. Cras eget leo sed nunc hendrerit ultricies eu at nisl. Praesent iaculis faucibus urna sit amet lacinia.</p>
  <div class="more">READ MORE ▸</div>
</article>

<footer class="abs footer">
  <div class="abs" style="left:145px;top:30px"><h4>Links</h4><ul><li>Home</li><li>Photography</li><li>Food</li><li>Beauty</li></ul></div>
  <div class="abs" style="left:274px;top:30px"><ul style="margin-top:27px"><li>RelationShips</li><li>Fitness</li><li>Technology</li><li>Real Estate</li></ul></div>
  <div class="abs vline" style="left:400px"></div>
  <div class="abs" style="left:441px;top:30px"><h4>Links</h4><ul><li>Contact us</li><li>About us</li><li>Terms and conditions</li><li>Privacy Police</li></ul></div>
  <div class="abs vline" style="left:598px"></div>
  <h4 class="abs" style="left:635px;top:30px">Newsletter Signup</h4>
  <div class="abs news">Email Address<b><svg width="26" height="36" viewBox="0 0 26 36"><path d="M10 12l6 6-6 6" stroke="#fff" stroke-width="2" fill="none"/></svg></b></div>
  <div class="abs vline" style="left:893px"></div>
  <h4 class="abs" style="left:930px;top:30px">Connect with us</h4>
  <div class="abs f-soc"><span style="background:#3b5998"></span><span style="background:#1da1f2"></span><span style="background:#0e76a8"></span><span style="background:#dd4b39"></span></div>
</footer>
<div class="abs copy">Copyright © 2016 &nbsp; Nine Pals per Month. &nbsp; All rights reserved.</div>

</body>
</html>
```